Business Card Design

I need a business card for my resume writing business. I have a logo that Im not keen on anymore so I would like the business card to use my photo instead of a logo. I am for mid career and trades resumes and prefer not to do executive resumes so don't need to aim for exectives. I would like it to be colourful. I like bright sky blue and maybe some pink or purple but primarily bright sky blue. I don't like green and Im keen see a fair bit of white on the card. As I have a photo to go it, it will need to go on a white background.

Target Market(s)

mid range careers. Not executives

Industry/Entity Type

Business

Contact Information for Business Card

Lise Varncombe
Resume Writer
Bright Path CVs
27 The Gullwing
HALDORN NSW 2391
lise@brightpathcvs.com.au
0417263958
www.brightpathcvs.com.au

Requirements
Nice to have
• Maybe colours similar to my website - www.brightpathcvs.com.au but not with any black on it.
Should not have
• No green or dark colours

```html
<!DOCTYPE html>
<html lang="en">
<head>
<meta charset="utf-8">
<title>Lise Varncombe – Business Card</title>
<link rel="stylesheet" href="https://fonts.googleapis.com/css2?family=Catamaran:wght@300;400&display=swap">
<style>
  :root {
    --page-bg: #d9d9d9;
    --card-bg: #ffffff;
    --sky-blue: #2f98d6;
    --accent-purple: #9a4fa6;
    --text-grey: #4a4a4a;
    --photo-light: #f1ebe7;
    --photo-mid: #c99d86;
    --photo-dark: #6a3a2c;
  }
  * { box-sizing: border-box; margin: 0; padding: 0; }
  html, body {
    width: 1200px; height: 985px; overflow: hidden;
    background: var(--page-bg);
    font-family: "Catamaran", sans-serif;
  }
  .business-card {
    position: absolute; left: 150px; top: 217px;
    width: 900px; height: 550px;
    background: var(--card-bg);
    border-radius: 36px;
    overflow: hidden;
    box-shadow: 0 6px 18px rgba(0,0,0,0.18);
  }
  .brand-band {
    position: absolute; left: 260px; top: 300px;
    width: 590px; height: 140px;
    background: var(--sky-blue);
  }
  .band-accent {
    position: absolute; left: 850px; top: 370px;
    width: 50px; height: 70px;
    background: var(--accent-purple);
  }
  .portrait {
    position: absolute; left: 30px; top: 40px;
    width: 300px; height: 510px;
    border-radius: 140px 140px 0 0;
    background: linear-gradient(180deg, var(--photo-dark) 0%, var(--photo-mid) 30%, var(--photo-light) 55%, var(--photo-light) 100%);
  }
  .contact-block {
    position: absolute; right: 50px; top: 120px;
    text-align: right;
  }
  .contact-address {
    color: var(--accent-purple);
    font-size: 22px; font-weight: 400;
    margin-bottom: 14px;
  }
  .contact-line {
    display: flex; justify-content: flex-end; align-items: center; gap: 12px;
    color: var(--text-grey);
    font-size: 24px; font-weight: 400; line-height: 34px;
  }
  .contact-icon {
    width: 22px; height: 22px; flex: none;
  }
  .identity {
    position: absolute; right: 60px; top: 322px;
    text-align: right; color: #ffffff;
  }
  .identity-name {
    font-size: 46px; font-weight: 300; line-height: 52px;
  }
  .identity-role {
    font-size: 22px; font-weight: 300; margin-top: 4px;
  }
</style>
</head>
<body>
  <main class="business-card">
    <div class="brand-band"></div>
    <div class="band-accent"></div>
    <div class="portrait" role="img" aria-label="Portrait photo of Lise Varncombe in a white jacket"></div>

    <section class="contact-block">
      <p class="contact-address">27 The Gullwing HALDORN NSW 2391</p>
      <p class="contact-line">0417263958
        <svg class="contact-icon" viewBox="0 0 22 22" aria-hidden="true">
          <rect width="22" height="22" rx="5" fill="var(--sky-blue)"/>
          <path d="M7 5 L9.5 5 L10.5 8.5 L9 9.8 Q10.5 12.8 12.7 13.8 L14 12.4 L17 13.5 L17 16 Q12 17.5 8 12.5 Q5.5 8.5 7 5 Z" fill="#fff"/>
        </svg>
      </p>
      <p class="contact-line">www.brightpathcvs.com.au
        <svg class="contact-icon" viewBox="0 0 22 22" aria-hidden="true">
          <rect width="22" height="22" rx="5" fill="var(--sky-blue)"/>
          <circle cx="11" cy="11" r="6" fill="none" stroke="#fff" stroke-width="1.5"/>
          <path d="M5 11 H17 M11 5 Q7.5 11 11 17 M11 5 Q14.5 11 11 17" fill="none" stroke="#fff" stroke-width="1.2"/>
        </svg>
      </p>
      <p class="contact-line">lise@brightpathcvs.com.au
        <svg class="contact-icon" viewBox="0 0 22 22" aria-hidden="true">
          <rect width="22" height="22" rx="5" fill="var(--sky-blue)"/>
          <rect x="5" y="7" width="12" height="8" rx="1" fill="none" stroke="#fff" stroke-width="1.5"/>
          <path d="M5 7.5 L11 12 L17 7.5" fill="none" stroke="#fff" stroke-width="1.3"/>
        </svg>
      </p>
    </section>

    <section class="identity">
      <h1 class="identity-name">Lise Varncombe</h1>
      <p class="identity-role">Resume Writer Bright Path CVs</p>
    </section>
  </main>
</body>
</html>
```